South Florida Real Estate Brokerage Business

The name is HOME CALVINA REAL ESTATE.
The company is a Real estate realty based in Miami.
Is targeted to Latin American clients.
Must express luxury, and efficiency.
Target clients for properties around 250k to a million +.
Calvina means Royal in Latin.
Should communicate safety and knowledge of the product and transaction with a tech edge.

The web design needs to be a Social tool, with Friendlane and other media integration of some sort. Needs to have a Show case place, a Search place (MLS listings) with maps and filters.
Needs to reflect luxury but also mixed with a social edge capable of engaging clients or transition them to communicate with the page.
Include the logo from the uploaded files, feel free to change the color or font per webdesign.
This is a Front en design, layout and graphics.
Possible future programming if approved.
I can receive Quotes for the Code part.

Target Market(s)

Spanish and English speakers living in Latin America and Canada looking for apartments and houses to buy.

Industry/Entity Type

Business

Requirements
Must have
• Search area.
Neighbourhood area.
Could be a blog or news area.
Client registration.
Social Plugin
Nice to have
• Social linking to networks.
Log in with friendlane account.
Friendlane Like.

```html
<!DOCTYPE html>
<html lang="en">
<head>
<meta charset="utf-8">
<title>Home Calvina Real Estate</title>
<link href="https://fonts.googleapis.com/css2?family=Arimo:wght@400;700&family=PT+Sans:wght@400&family=Tenor+Sans&family=Tinos:wght@700&family=Ubuntu:wght@300;400;500&display=swap" rel="stylesheet">
<style>
:root{
  --bg-dark:#2a2627;
  --frame-dark:#231f20;
  --page:#ffffff;
  --gold:#c79a3b;
  --gold-soft:#d4b06a;
  --text:#333333;
  --muted:#666666;
  --light-grey:#e8e8e8;
  --tab-dark:#3a3a3a;
  --green-top:#63bd2c;
  --green-bottom:#2f8a10;
  --orange:#e05a2b;
  --red:#d2492a;
  --footer-text:#a9a6a6;
  --news-orange:#c8692d;
}
*{box-sizing:border-box;margin:0;padding:0}
html,body{width:952px;height:1200px;overflow:hidden}
body{background:var(--bg-dark);font-family:"Arimo",Arial,sans-serif;color:var(--text);position:relative}
.abs{position:absolute}
.page{position:absolute;left:104px;top:0;width:742px;height:952px;background:var(--page)}
.canvas{position:absolute;left:0;top:0;width:952px;height:1200px}

/* header */
.brand-name{left:116px;top:78px;width:172px;text-align:center;font-family:"Ubuntu",sans-serif;font-weight:400;color:var(--gold);font-size:17px;line-height:20px;letter-spacing:.5px;white-space:nowrap}
.login-label{font-size:9.5px;color:var(--muted);top:9px}
.login-input{top:22px;height:20px;background:var(--light-grey)}
.login-btn{left:789px;top:22px;width:42px;height:21px;background:#111;color:#fff;font-size:11px;line-height:21px;text-align:center}
.remember-box{left:466px;top:50px;width:10px;height:10px;background:#d6d6d6}
.small-link{font-size:9.5px;color:var(--muted)}
.nav{top:100px;left:304px;font-family:"Ubuntu",sans-serif;font-size:10.5px;color:#555;text-transform:uppercase}
.nav-item{position:absolute;white-space:nowrap;top:0}
.nav-item.active{color:var(--gold)}
.nav-sep{position:absolute;top:-1px;width:1px;height:17px;background:#bbb}

/* hero */
.hero-frame{left:111px;top:132px;width:728px;height:317px;background:var(--frame-dark)}
.hero-photo{left:119px;top:140px;width:712px;height:301px;background:linear-gradient(180deg,#a9c3df 0%,#c9d4df 35%,#b9c0c6 55%,#6f8e4d 80%,#4f7a2e 100%)}
.hero-arrow{width:52px;height:52px;border-radius:50%;background:var(--frame-dark)}
.hero-arrow span{position:absolute;left:6px;top:6px;width:40px;height:40px;border-radius:50%;background:var(--gold-soft)}
.hero-arrow svg{position:absolute;left:14px;top:14px}

/* search */
.tab{top:465px;height:29px;font-family:"Tinos",serif;font-weight:700;font-size:10.5px;line-height:29px;text-align:center;letter-spacing:.2px}
.tab.on{background:#f5f5f5;border:1px solid #ccc;border-bottom:none;color:#222}
.tab.off{background:var(--tab-dark);color:#fff}
.search-panel{left:111px;top:493px;width:728px;height:73px;background:linear-gradient(#f8f8f8,#e6e6e6);border:1px solid #d8d8d8}
.radio{width:9px;height:9px;border-radius:50%;border:1px solid #999;background:#fff}
.radio.on::after{content:"";position:absolute;left:1px;top:1px;width:5px;height:5px;border-radius:50%;background:#3a6fb0}
.field-label{font-size:10px;color:#333;text-align:right;white-space:nowrap}
.select{height:14px;background:#fff;border:1px solid #aaa;font-size:8px;line-height:12px;padding-left:3px;color:#222}
.select::after{content:"";position:absolute;right:4px;top:4px;border-left:3px solid transparent;border-right:3px solid transparent;border-top:4px solid #333}
.search-btn{left:702px;top:509px;width:121px;height:25px;border-radius:4px;background:linear-gradient(var(--green-top),var(--green-bottom));color:#fff;font-family:"Ubuntu",sans-serif;font-size:11px;line-height:25px;padding-left:7px}
.search-btn svg{position:absolute;right:7px;top:5px}
.advanced{left:748px;top:537px;font-size:9px;color:#333;text-decoration:underline}

/* welcome */
.welcome-bar{left:111px;top:589px;width:7px;height:28px;background:#333}
.welcome-head{left:118px;top:589px;width:360px;height:28px;background:linear-gradient(90deg,#e6e6e6,#ffffff);font-family:"Tenor Sans",sans-serif;font-size:17px;line-height:28px;padding-left:9px;letter-spacing:.8px;color:#222;white-space:nowrap}
.welcome-copy{left:111px;top:624px;width:366px;font-family:"PT Sans",sans-serif;font-size:9.8px;line-height:13.5px;color:#333}
.welcome-copy p+p{margin-top:13px}
.more{font-size:8.5px;color:#444}

/* news */
.news-title{left:498px;top:584px;font-family:"Ubuntu",sans-serif;font-weight:300;font-size:16px;color:#222}
.cal{width:47px;height:46px;border-radius:4px;background:linear-gradient(#fff,#e6e6e6);border:1px solid #ccc;box-shadow:0 2px 2px rgba(0,0,0,.15);text-align:center}
.cal-top{height:15px;background:var(--news-orange);color:#fff;font-size:7px;line-height:17px;border-radius:3px 3px 0 0}
.cal-day{font-family:"Tinos",serif;font-size:17px;color:#333;line-height:26px}
.news-head{font-family:"Arimo",sans-serif;font-size:12px;color:#111;white-space:nowrap}
.news-text{font-size:10px;line-height:14px;color:#555;width:275px}

.divider{left:210px;top:749px;width:520px;height:1px;background:linear-gradient(90deg,rgba(0,0,0,0),#ddd,rgba(0,0,0,0))}
.gallery-title{left:104px;top:768px;width:742px;text-align:center;font-family:"Tenor Sans",sans-serif;font-size:17px;letter-spacing:1px;color:#333}
.thumb{top:803px;width:136px;height:134px;background:#e3e3e3}
.thumb span{position:absolute;left:9px;top:9px;width:118px;height:116px}
.circle-arrow{top:860px;width:25px;height:25px}

/* footer */
.newsletter{left:111px;top:976px;font-family:"Ubuntu",sans-serif;font-size:14px;color:#d4a94e}
.nl-input{left:283px;top:976px;width:128px;height:20px;background:#fff;font-size:8.5px;line-height:20px;padding-left:6px;color:#444}
.nl-btn{left:411px;top:976px;width:43px;height:20px;background:var(--red);color:#fff;font-size:9px;line-height:20px;text-align:center}
.foot-rule{left:111px;top:1019px;width:490px;height:1px;background:#3a3536}
.foot-head{top:1030px;font-size:8.5px;color:var(--orange);text-transform:uppercase}
.foot-list{top:1049px;font-size:8.5px;line-height:13.4px;color:var(--footer-text);list-style:none}
.foot-list .hl{color:var(--orange)}
.blog-date{font-size:8px;color:var(--orange)}
.blog-text{font-size:8.5px;color:var(--footer-text)}
.copyright{left:113px;top:1176px;font-size:8.5px;color:var(--footer-text)}
.social-sq{top:1174px;width:12px;height:12px;border-radius:2px}

/* social plugin */
.plugin{left:646px;top:978px;width:192px;height:180px;background:#fff;border:1px solid #b8b8b8}
.plugin-mark{left:7px;top:8px;width:31px;height:30px;background:#2e2a22}
.plugin-title{left:52px;top:10px;font-size:8px;color:#333}
.plugin-title b{color:#3b5998;font-weight:700}
.like-btn{left:44px;top:22px;width:35px;height:16px;border:1px solid #bbb;border-radius:2px;background:linear-gradient(#fff,#eee);font-size:8px;line-height:14px;text-align:center;color:#333}
.signup-btn{left:138px;top:21px;width:46px;height:19px;background:linear-gradient(#6fbf45,#3f9a22);border:1px solid #2f7f15;color:#fff;font-size:9.5px;line-height:17px;text-align:center}
.plugin-count{left:7px;top:52px;font-size:8px;color:#333}
.plugin-rule{left:6px;width:180px;height:1px;background:#ddd}
.member{width:32px;text-align:center;font-size:8px;color:#333}
.member span{display:block;width:30px;height:30px;margin:0 auto 4px}
.plugin-foot{left:7px;top:166px;font-size:6.5px;color:#555}
.plugin-foot i{display:inline-block;width:8px;height:8px;background:#3b5998;vertical-align:-1px;margin-right:3px}
</style>
</head>
<body>
<div class="page"></div>
<div class="canvas">

  <header>
    <div class="abs brand-name">HOME CALVINA<br>REAL ESTATE</div>

    <div class="abs login-label" style="left:466px">User ID</div>
    <div class="abs login-input" style="left:466px;width:154px"></div>
    <div class="abs login-label" style="left:627px">Password</div>
    <div class="abs login-input" style="left:627px;width:155px"></div>
    <div class="abs login-btn">Log in</div>
    <div class="abs remember-box"></div>
    <div class="abs small-link" style="left:482px;top:50px">Remember me</div>
    <div class="abs small-link" style="left:627px;top:50px">Forgot your Password ? / Register</div>

    <nav class="abs nav">
      <span class="nav-item active" style="left:0">Home</span>
      <span class="nav-sep" style="left:45px"></span>
      <span class="nav-item" style="left:60px">Company</span>
      <span class="nav-sep" style="left:123px"></span>
      <span class="nav-item" style="left:139px">Associates</span>
      <span class="nav-sep" style="left:210px"></span>
      <span class="nav-item" style="left:226px">Search Properties</span>
      <span class="nav-sep" style="left:337px"></span>
      <span class="nav-item" style="left:354px">Marketing &amp;Design</span>
      <span class="nav-sep" style="left:468px"></span>
      <span class="nav-item" style="left:484px">Contact</span>
    </nav>
  </header>

  <section>
    <div class="abs hero-frame"></div>
    <div class="abs hero-photo" role="img" aria-label="Photo of a large grey two-storey family house with a porch and flowering garden"></div>
    <div class="abs hero-arrow" style="left:117px;top:264px"><span></span>
      <svg width="24" height="24" viewBox="0 0 24 24"><path d="M14 6 L8 12 L14 18" fill="none" stroke="#3a2f1c" stroke-width="2"/></svg></div>
    <div class="abs hero-arrow" style="left:780px;top:264px"><span></span>
      <svg width="24" height="24" viewBox="0 0 24 24"><path d="M10 6 L16 12 L10 18" fill="none" stroke="#3a2f1c" stroke-width="2"/></svg></div>
  </section>

  <section>
    <div class="abs tab on" style="left:111px;width:116px">PROPERTY SEARCH</div>
    <div class="abs tab off" style="left:229px;width:125px">OPEN HOUSE SEARCH</div>
    <div class="abs tab off" style="left:357px;width:84px">MAP SEARCH</div>
    <div class="abs search-panel"></div>

    <div class="abs radio on" style="left:126px;top:509px"></div>
    <div class="abs field-label" style="left:142px;top:508px">For Sale</div>
    <div class="abs radio" style="left:126px;top:537px"></div>
    <div class="abs field-label" style="left:142px;top:536px">For Rent</div>

    <div class="abs field-label" style="left:217px;top:511px;width:80px">Property Type</div>
    <div class="abs select" style="left:304px;top:509px;width:77px">Condominiums</div>
    <div class="abs field-label" style="left:217px;top:536px;width:80px">City Name</div>
    <div class="abs select" style="left:304px;top:534px;width:77px">Miami Beach</div>

    <div class="abs field-label" style="left:420px;top:511px;width:63px">Price Min</div>
    <div class="abs select" style="left:490px;top:509px;width:57px">$250.000</div>
    <div class="abs field-label" style="left:420px;top:536px;width:63px">Price Max</div>
    <div class="abs select" style="left:490px;top:534px;width:57px">$5 M+</div>

    <div class="abs field-label" style="left:600px;top:511px;width:40px">Beds</div>
    <div class="abs select" style="left:643px;top:509px;width:28px">1+</div>
    <div class="abs field-label" style="left:600px;top:536px;width:40px">Baths</div>
    <div class="abs select" style="left:643px;top:534px;width:28px">1+</div>

    <div class="abs search-btn">Property Search
      <svg width="14" height="14" viewBox="0 0 14 14"><circle cx="5.5" cy="5.5" r="4" fill="none" stroke="#13380a" stroke-width="2"/><path d="M8.5 8.5 L12.5 12.5" stroke="#13380a" stroke-width="2.4"/></svg>
    </div>
    <div class="abs advanced">Advanced Search</div>
  </section>

  <section>
    <div class="abs welcome-bar"></div>
    <h1 class="abs welcome-head" style="font-weight:400">WELCOME TO HOME CALVINA</h1>
    <div class="abs welcome-copy">
      <p>Lorem Ipsum is simply dummy text of the printing and typesetting industry. Lorem Ipsum has been the industry's standard dummy text ever since the 1500s, when an unknown printer took a of type and scrambled it to make a type specimen book.</p>
      <p>Lorem Ipsum comes from sections 1.10.32 and 1.10.33 of "de Finibus Bonorum et Malorum" (The Extremes of Good and Evil) by Cicero, written in 45 BC. This book is a treatise on the theory of ethics, very popular during the Renaissance.</p>
    </div>
    <div class="abs more" style="left:423px;top:727px">Read More &#8594;</div>
  </section>

  <section>
    <h2 class="abs news-title">LATEST NEWS</h2>
    <div class="abs cal" style="left:498px;top:612px"><div class="cal-top">AUG</div><div class="cal-day">21</div></div>
    <div class="abs news-head" style="left:562px;top:614px">Lorem Ipsum is simply dummy text setting industry.</div>
    <div class="abs news-text" style="left:562px;top:633px">Lorem Ipsum is simply dummy text of the printing&nbsp; Ipsum has been the dummy text ever since the 1500s...</div>
    <div class="abs cal" style="left:498px;top:672px"><div class="cal-top">AUG</div><div class="cal-day">21</div></div>
    <div class="abs news-head" style="left:562px;top:674px">Lorem Ipsum is simply dummy text setting industry.</div>
    <div class="abs news-text" style="left:562px;top:693px">Lorem Ipsum is simply dummy text of the printing&nbsp; Ipsum has been the dummy text ever since the 1500s...</div>
    <div class="abs more" style="left:780px;top:727px">View All News &#8594;</div>
  </section>

  <div class="abs divider"></div>

  <section>
    <h2 class="abs gallery-title" style="font-weight:400">PHOTO GALLERY</h2>
    <svg class="abs circle-arrow" style="left:120px" viewBox="0 0 25 25"><circle cx="12.5" cy="12.5" r="11" fill="#fff" stroke="#111" stroke-width="2"/><path d="M18 12.5 H8 M12 8 L7.5 12.5 L12 17" fill="none" stroke="#111" stroke-width="2.4"/></svg>
    <div class="abs thumb" style="left:160px"><span role="img" aria-label="Photo of a modern white apartment building" style="background:linear-gradient(#6fa6d8,#dfe9f2 55%,#9fb48a)"></span></div>
    <div class="abs thumb" style="left:324px"><span role="img" aria-label="Photo of a residential tower against blue sky" style="background:linear-gradient(#2f6fb8,#8bb8e0 55%,#b3b3b0)"></span></div>
    <div class="abs thumb" style="left:488px"><span role="img" aria-label="Photo of a suburban family house with front lawn" style="background:linear-gradient(#c8d6e4,#a59d93 55%,#5e8a3a)"></span></div>
    <div class="abs thumb" style="left:652px"><span role="img" aria-label="Photo of a large house with turrets and garden" style="background:linear-gradient(#dfe6ea,#a7a79a 55%,#4f7f33)"></span></div>
    <svg class="abs circle-arrow" style="left:806px" viewBox="0 0 25 25"><circle cx="12.5" cy="12.5" r="11" fill="#fff" stroke="#111" stroke-width="2"/><path d="M7 12.5 H17 M13 8 L17.5 12.5 L13 17" fill="none" stroke="#111" stroke-width="2.4"/></svg>
  </section>

  <footer>
    <div class="abs newsletter">Sign Up Our Newsletter!</div>
    <div class="abs nl-input">Enter Your E-mail...</div>
    <div class="abs nl-btn">Sign Up</div>
    <div class="abs foot-rule"></div>

    <div class="abs foot-head" style="left:112px">Quick Links</div>
    <ul class="abs foot-list" style="left:112px">
      <li>Home</li><li>Company</li><li>Associates</li><li>Search Properties</li><li>Marketing &amp;Design</li><li>Contact</li>
    </ul>

    <div class="abs foot-head" style="left:257px">Contact Us</div>
    <ul class="abs foot-list" style="left:261px">
      <li>012 Lorem Ipsum,</li><li>dummy text.</li><li>(000) 123-4567 Phone</li><li>(000) 123-4567 Fax</li><li class="hl">Email-info@calvinahomes.example</li>
    </ul>

    <div class="abs foot-head" style="left:458px">Recent Blog Post</div>
    <div class="abs blog-date" style="left:458px;top:1052px">12 March, 2012</div>
    <div class="abs blog-text" style="left:458px;top:1065px">Lorem Ipsum is simply dummy text...</div>
    <div class="abs blog-date" style="left:458px;top:1092px">12 March, 2012</div>
    <div class="abs blog-text" style="left:458px;top:1105px">Lorem Ipsum is simply dummy text...</div>
    <div class="abs blog-date" style="left:458px;top:1132px">12 March, 2012</div>
    <div class="abs blog-text" style="left:458px;top:1145px">Lorem Ipsum is simply dummy text...</div>

    <div class="abs copyright">&copy; 2012 Home Calvina. | All Rights Reserved.</div>
    <div class="abs social-sq" style="left:786px;background:#3b5998"></div>
    <div class="abs social-sq" style="left:806px;background:#3fa9db"></div>
    <div class="abs social-sq" style="left:826px;background:#2a79b3"></div>

    <aside class="abs plugin">
      <div class="abs plugin-mark"></div>
      <div class="abs plugin-title"><b>Home Calvina</b> on Friendlane</div>
      <div class="abs like-btn">Like</div>
      <div class="abs signup-btn">Sign Up</div>
      <div class="abs plugin-count">560 people like &nbsp;<b>Home Calvina</b></div>
      <div class="abs plugin-rule" style="top:46px"></div>

      <div class="abs member" style="left:6px;top:65px"><span role="img" aria-label="Member photo" style="background:#d9a6a0"></span>Selva</div>
      <div class="abs member" style="left:47px;top:65px"><span role="img" aria-label="Member photo" style="background:#8fa6b8"></span>Orlan</div>
      <div class="abs member" style="left:88px;top:65px"><span role="img" aria-label="Member photo" style="background:#5a4038"></span>Anika</div>
      <div class="abs member" style="left:129px;top:65px"><span role="img" aria-label="Member photo" style="background:#a88a70"></span>Mirel</div>
      <div class="abs member" style="left:6px;top:117px"><span role="img" aria-label="Member photo" style="background:#b27a8c"></span>Lina</div>
      <div class="abs member" style="left:47px;top:117px"><span role="img" aria-label="Member photo" style="background:#8a9a6c"></span>Bram</div>
      <div class="abs member" style="left:88px;top:117px"><span role="img" aria-label="Member photo" style="background:#7a6a78"></span>Roxana</div>
      <div class="abs member" style="left:129px;top:117px"><span role="img" aria-label="Member photo" style="background:#9c6a4e"></span>Zeno</div>

      <div class="abs plugin-rule" style="top:161px"></div>
      <div class="abs plugin-foot"><i></i>Friendlane social plugin</div>
    </aside>
  </footer>
</div>
</body>
</html>
```